I am a general contractor in Portland, Or. I would like a clean and simple design layout, maybe using the "didot" font, blue and dark bronze in colors are preferred. On one side of the card, it would be nice to have a logo(attached photo) and business name(Brenwick Construction). I don't need my job title on the card, just some thing along the lines of "oliver kemp, general contractor". Thanks much.

Target Market(s)

Adults from 30-55 years old. Middle to upper class.

Industry/Entity Type

Contractor

Contact Information for Business Card

Brenwick Construction
Oliver T. Kemp
2843 NE 71st Ave.
Portland, Or. 97348
503.962.7084

Font styles to use
Other font styles liked:
• didot

Colors
3277b5
7f7f7f

Requirements
Should not have
• Too much going on.

```html
<!DOCTYPE html>
<html lang="en">
<head>
<meta charset="utf-8">
<title>Brenwick Construction – Business Card</title>
<link rel="stylesheet" href="https://fonts.googleapis.com/css2?family=Exo+2:wght@400;500;700;800&display=swap">
<style>
  :root {
    --page-bg: #e4e5e7;
    --card-white: #ffffff;
    --navy: #1f2f78;
    --sky: #3b9fe0;
    --swoosh-grey: #6f7177;
    --text-light: #ffffff;
    --shadow: rgba(20, 25, 45, 0.18);
  }
  * { box-sizing: border-box; margin: 0; padding: 0; }
  html, body {
    width: 1200px;
    height: 771px;
    overflow: hidden;
    background: var(--page-bg);
    font-family: "Exo 2", Arial, sans-serif;
  }
  .canvas {
    position: relative;
    width: 1200px;
    height: 771px;
    display: flex;
    align-items: center;
    justify-content: center;
    gap: 60px;
  }
  .card {
    position: relative;
    width: 520px;
    height: 297px;
    background: var(--card-white);
    box-shadow: 0 10px 28px var(--shadow);
    overflow: hidden;
  }

  /* Front side */
  .brand {
    position: absolute;
    inset: 0;
    display: flex;
    align-items: center;
    justify-content: center;
    gap: 22px;
  }
  .brand-dot {
    width: 86px;
    height: 86px;
    border-radius: 50%;
    background: var(--sky);
    flex: none;
  }
  .brand-name {
    color: var(--navy);
    font-weight: 800;
    font-size: 40px;
    line-height: 1.02;
    letter-spacing: 0.5px;
  }

  /* Back side */
  .back-shape {
    position: absolute;
    inset: 0;
    width: 100%;
    height: 100%;
  }
  .contact {
    position: absolute;
    left: 34px;
    top: 34px;
    color: var(--text-light);
  }
  .contact-name {
    font-weight: 500;
    font-size: 19px;
    letter-spacing: 1.6px;
    text-transform: uppercase;
  }
  .contact-role {
    font-size: 13px;
    letter-spacing: 0.6px;
    margin-top: 3px;
  }
  .contact-address {
    font-size: 13px;
    letter-spacing: 0.6px;
    line-height: 1.45;
    margin-top: 22px;
  }
  .contact-list {
    list-style: none;
    margin-top: 18px;
    font-size: 12.5px;
    letter-spacing: 0.6px;
  }
  .contact-list li {
    display: flex;
    align-items: center;
    gap: 9px;
    line-height: 1.75;
  }
  .contact-list svg {
    width: 12px;
    height: 12px;
    flex: none;
  }
  .back-brand {
    position: absolute;
    right: 36px;
    top: 152px;
    display: flex;
    align-items: center;
    gap: 10px;
  }
  .back-brand .brand-dot {
    width: 28px;
    height: 28px;
  }
  .back-brand-name {
    color: var(--navy);
    font-weight: 800;
    font-size: 24px;
    letter-spacing: 0.5px;
  }
</style>
</head>
<body>
<main class="canvas">

  <section class="card card-front" aria-label="Front of business card">
    <div class="brand">
      <span class="brand-dot" aria-hidden="true"></span>
      <h1 class="brand-name">Brenwick<br>Construction</h1>
    </div>
  </section>

  <section class="card card-back" aria-label="Back of business card">
    <svg class="back-shape" viewBox="0 0 520 297" preserveAspectRatio="none" aria-hidden="true">
      <defs>
        <linearGradient id="panel-fill" x1="0" y1="0" x2="1" y2="1">
          <stop offset="0" stop-color="#2a3f95"/>
          <stop offset="0.55" stop-color="#34509f"/>
          <stop offset="1" stop-color="#1f2f78"/>
        </linearGradient>
      </defs>
      <path d="M0 0 H372 C318 70 282 170 282 297 H0 Z" fill="url(#panel-fill)"/>
      <path d="M372 0 H392 C336 72 300 172 296 297 H282 C282 170 318 70 372 0 Z" fill="var(--swoosh-grey)"/>
    </svg>

    <div class="contact">
      <h2 class="contact-name">Oliver T. Kemp</h2>
      <p class="contact-role">General Contractor</p>
      <p class="contact-address">2843 NE 71st Ave.<br>Portland, Or. 97348</p>
      <ul class="contact-list">
        <li>
          <svg viewBox="0 0 12 12"><path d="M3 1 L5 3.5 L4 5 Q5 7 7 8 L8.5 7 L11 9 L9.5 11 Q5 10.5 1.5 5 Q1 3 3 1 Z" fill="#fff"/></svg>
          503.962.7084
        </li>
        <li>
          <svg viewBox="0 0 12 12"><rect x="3" y="0.5" width="6" height="11" rx="1" fill="none" stroke="#fff" stroke-width="1.2"/><circle cx="6" cy="9.5" r="0.8" fill="#fff"/></svg>
          503.962.7085
        </li>
        <li>
          <svg viewBox="0 0 12 12"><rect x="0.6" y="2.5" width="10.8" height="7" fill="none" stroke="#fff" stroke-width="1.2"/><path d="M0.6 2.5 L6 6.5 L11.4 2.5" fill="none" stroke="#fff" stroke-width="1.2"/></svg>
          oliver@brenwickbuild.com
        </li>
        <li>
          <svg viewBox="0 0 12 12"><circle cx="6" cy="6" r="5.2" fill="none" stroke="#fff" stroke-width="1.1"/><ellipse cx="6" cy="6" rx="2.3" ry="5.2" fill="none" stroke="#fff" stroke-width="1"/><path d="M0.8 6 H11.2" stroke="#fff" stroke-width="1"/></svg>
          www.brenwickbuild.com
        </li>
      </ul>
    </div>

    <div class="back-brand">
      <span class="brand-dot" aria-hidden="true"></span>
      <span class="back-brand-name">Brenwick</span>
    </div>
  </section>

</main>
</body>
</html>
```